Trade Show Booth Sign Design for Retracting Banner

I need a trade show booth sign designed. It will be for a retractable banner that is double sided with 34 by 81 inch.

I want to incorporate my logo (see attached, have it in other file formats as well) and graphics from my website (https://www.pellacorvaadvisory.com/) with parts or all of the following text.

· Educational Content Creation
o Supplemental Textbook Content Development
o E-learning Content Development
· Curriculum Development
o VKTR/Joint Pillar
o Three Dimensional Learning
· Assessment
o Formative Assessments
o Elementary School, Middle School, High School, College, and Business
· Professional Development
o Training
o Facilitation

Target Market(s)

Education

Industry/Entity Type

Education

Font styles to use
Sans Serif

Colors

Designer to choose colors to be used in the design.

Requirements
Must have
• Eye catching and easy to read design
Nice to have
• Would like to see incorporation of my logo and some of the elements of my website images
Should not have
• N/A

```html
<!DOCTYPE html>
<html lang="en">
<head>
<meta charset="utf-8">
<title>Pellacorva Advisory – Retractable Banner</title>
<link href="https://fonts.googleapis.com/css2?family=Oswald:wght@700&family=Montserrat:wght@600&display=swap" rel="stylesheet">
<style>
  :root {
    --navy: #1c2a5e;
    --blue: #3a86c8;
    --panel: #e9e8ea;
    --white: #ffffff;
    --stage: #f4f4f4;
  }
  * { box-sizing: border-box; margin: 0; padding: 0; }
  html, body { width: 1200px; height: 900px; overflow: hidden; background: var(--stage); }
  .banner {
    position: absolute; left: 410px; top: 20px;
    width: 380px; height: 860px;
    background: var(--white);
    box-shadow: 0 2px 10px rgba(0,0,0,.12);
    overflow: hidden;
  }
  .brand-band {
    position: absolute; left: 0; top: 42px; width: 380px; height: 128px;
    background: var(--navy);
  }
  .brand-disc {
    position: absolute; left: 12px; top: 28px; width: 152px; height: 152px;
    border-radius: 50%; background: var(--white); border: 6px solid var(--navy);
  }
  .brand-name {
    position: absolute; left: 172px; top: 66px; width: 196px;
    font-family: "Oswald", sans-serif; font-weight: 700; color: var(--white);
    text-align: right; line-height: 1; white-space: nowrap;
  }
  .brand-name .main { display: block; font-size: 32px; letter-spacing: .5px; }
  .brand-name .sub { display: block; font-size: 18px; margin-top: 10px; letter-spacing: 1px; }
  .idea-art {
    position: absolute; left: 10px; top: 182px; width: 360px; height: 118px;
    border-radius: 12px;
    background: radial-gradient(circle at 50% 55%, #f6c431 0 12%, transparent 30%),
                linear-gradient(90deg, #e8453a 0%, #5470c9 28%, #f3e6b0 50%, #f08a2c 75%, #6cc0e8 100%);
    opacity: .55;
  }
  .tagline {
    position: absolute; left: 0; top: 312px; width: 350px; height: 46px;
    background: var(--blue);
    clip-path: polygon(0 0, 100% 0, 94% 100%, 0 100%);
    font-family: "Oswald", sans-serif; font-weight: 700; color: var(--white);
    font-size: 26px; letter-spacing: 2px; line-height: 46px; padding-left: 34px;
  }
  .services {
    position: absolute; left: 0; top: 372px; width: 380px; height: 430px;
    background: var(--panel);
    padding: 16px 20px 0 24px;
    display: flex; flex-direction: column; gap: 12px;
  }
  .service { position: relative; }
  .service h2 {
    font-family: "Oswald", sans-serif; font-weight: 700; color: var(--navy);
    font-size: 23px; line-height: 26px; text-transform: uppercase; white-space: nowrap;
    border-bottom: 3px solid var(--blue); padding-bottom: 3px; margin-bottom: 8px;
  }
  .service.content h2, .service.assessment h2 { width: 240px; }
  .service ul { list-style: none; display: flex; flex-direction: column; gap: 8px; }
  .service.content ul, .service.assessment ul { max-width: 240px; }
  .service li {
    display: flex; align-items: flex-start; gap: 10px;
    font-family: "Montserrat", sans-serif; font-weight: 600; font-size: 12px;
    line-height: 15px; color: var(--navy);
  }
  .service li svg { flex: none; width: 18px; height: 15px; }
  .service.pro ul { flex-direction: row; gap: 70px; }
  .scene-badge {
    position: absolute; right: 0; width: 88px; height: 88px; border-radius: 50%;
    background: radial-gradient(circle at 50% 45%, #5a79b8 0%, var(--navy) 70%);
    border: 4px solid #cfd3dc;
  }
  .scene-badge.teaching { top: -6px; }
  .scene-badge.science { top: 6px; }
  .footer {
    position: absolute; left: 0; top: 802px; width: 380px; height: 58px;
    background: var(--navy); color: var(--white);
    font-family: "Montserrat", sans-serif; font-weight: 600; font-size: 16px;
    display: flex; align-items: center; justify-content: center;
  }
</style>
</head>
<body>
<div class="banner">
  <div class="brand-band"></div>
  <div class="brand-disc"></div>
  <div class="brand-name"><span class="main">PELLACORVA</span><span class="sub">ADVISORY</span></div>

  <div class="idea-art" role="img" aria-label="Row of crumpled paper light bulbs in red, blue, yellow, orange and light blue, the yellow one glowing"></div>

  <div class="tagline">LEARN. GROW. KNOW.</div>

  <div class="services">
    <section class="service content">
      <h2>Educational<br>Content Creation</h2>
      <ul>
        <li><svg viewBox="0 0 18 15"><path d="M1 8l5 5L17 1" fill="none" stroke="#3a86c8" stroke-width="3"/></svg>Supplemental Textbook Content Development</li>
        <li><svg viewBox="0 0 18 15"><path d="M1 8l5 5L17 1" fill="none" stroke="#3a86c8" stroke-width="3"/></svg>E-learning Content Development</li>
      </ul>
      <div class="scene-badge teaching" role="img" aria-label="Illustration of a presenter beside a chart board in front of a seated audience"></div>
    </section>
    <section class="service curriculum">
      <h2>Curriculum Development</h2>
      <ul>
        <li><svg viewBox="0 0 18 15"><path d="M1 8l5 5L17 1" fill="none" stroke="#3a86c8" stroke-width="3"/></svg>VKTR/Joint Pillar</li>
        <li><svg viewBox="0 0 18 15"><path d="M1 8l5 5L17 1" fill="none" stroke="#3a86c8" stroke-width="3"/></svg>Three Dimensional Learning</li>
      </ul>
    </section>
    <section class="service assessment">
      <h2>Assessment</h2>
      <ul>
        <li><svg viewBox="0 0 18 15"><path d="M1 8l5 5L17 1" fill="none" stroke="#3a86c8" stroke-width="3"/></svg>Formative Assessments</li>
        <li><svg viewBox="0 0 18 15"><path d="M1 8l5 5L17 1" fill="none" stroke="#3a86c8" stroke-width="3"/></svg>Elementary School, Middle School, High School, College, and Business</li>
      </ul>
      <div class="scene-badge science" role="img" aria-label="Illustration of science and learning icons around a lab flask"></div>
    </section>
    <section class="service pro">
      <h2>Professional Development</h2>
      <ul>
        <li><svg viewBox="0 0 18 15"><path d="M1 8l5 5L17 1" fill="none" stroke="#3a86c8" stroke-width="3"/></svg>Training</li>
        <li><svg viewBox="0 0 18 15"><path d="M1 8l5 5L17 1" fill="none" stroke="#3a86c8" stroke-width="3"/></svg>Facilitation</li>
      </ul>
    </section>
  </div>

  <div class="footer">www.PellaCorvaAdvisory.com</div>
</div>
</body>
</html>
```